Thornwell Building Company - advertisement poster

I am looking to print some canvas signs to advertise my general contracting company, Thornwell Building Company. The sign will measure 6' long x 3' high so the size should match that ratio. I already have a logo icon, which is the Letter 'A' and some trees that I would like to incorporate, see attached. I would also like the to have the following information listed:
1) phone number: 472-318-6095
2) email: thornwellbuildingcompany@mailvistra.net
3) website: thornwellbuildingcompany.com
4) Lic#5386204
5) I want to use this text: "BUILD WITH THE T-CREW!"

The ad should be relatively simple and clean. Black and Green are my company colors. I am open to creative ideas!

Target Market(s)

People looking to renovate their homes

Industry/Entity Type

Construction

Colors
59FF00
82FF00
B8FF75
E3FFCB
F4FFEA

Requirements
Must have
• Must have my company logo
Should not have
• No photos or complex graphics

```html
<!DOCTYPE html>
<html lang="en">
<head>
<meta charset="utf-8">
<title>Thornwell Building Company – Sign</title>
<link rel="stylesheet" href="https://fonts.googleapis.com/css2?family=Open+Sans:wdth,wght@75..100,600..800&display=swap">
<style>
  :root {
    --page: #ffffff;
    --ink: #000000;
    --navy: #1a1f66;
    --white: #ffffff;
    --brand-green: #6aaf32;
    --lime: #82ff00;
    --neon: #59ff00;
    --pale: #b8ff75;
    --mist: #f4ffea;
    --tint: #d2ff9c;
    --rule: #5ff01a;
  }
  * { margin: 0; padding: 0; box-sizing: border-box; }
  html, body {
    width: 1200px; height: 927px; overflow: hidden;
    background: var(--page);
    font-family: "Open Sans", Arial, sans-serif;
  }
  .sign {
    position: absolute; left: 46px; top: 186px;
    width: 1109px; height: 556px;
    border: 1px solid var(--ink);
    overflow: hidden;
  }
  .sign-shapes { position: absolute; inset: 0; }
  .text { position: absolute; line-height: 1; white-space: nowrap; text-align: center; }

  .brand-mark {
    position: absolute; left: 236px; top: 282px;
    width: 80px; height: 80px; background: var(--brand-green);
  }
  .brand-name { left: 96px; width: 360px; color: var(--white); font-weight: 700; }
  .brand-name--main { top: 392px; font-size: 42px; letter-spacing: 1px; }
  .brand-name--sub { top: 444px; font-size: 20px; letter-spacing: 6px; }

  .phone {
    left: 56px; width: 440px; top: 499px;
    font-size: 63px; font-weight: 700; color: var(--white);
  }
  .licence {
    left: 126px; width: 300px; top: 641px;
    font-size: 26px; font-weight: 700; color: var(--white);
  }

  .headline {
    left: 531px; width: 600px;
    font-weight: 800; color: var(--ink); font-stretch: 85%;
    -webkit-text-stroke: 1px var(--white); paint-order: stroke fill;
  }
  .headline--top { top: 262px; font-size: 77px; letter-spacing: -1px; }
  .headline--main { top: 346px; font-size: 98px; letter-spacing: -1px; }

  .contact { left: 531px; width: 600px; color: var(--navy); font-weight: 700; }
  .contact-label { font-size: 24px; }
  .contact-label--email { top: 468px; }
  .contact-value--email { top: 505px; font-size: 23px; }
  .contact-rule {
    position: absolute; left: 582px; top: 556px;
    width: 495px; height: 4px; background: var(--rule);
  }
  .contact-label--web { top: 580px; }
  .contact-value--web { top: 618px; font-size: 26px; }
</style>
</head>
<body>
  <div class="sign">
    <svg class="sign-shapes" viewBox="0 0 1109 556" width="1109" height="556" aria-hidden="true">
      <defs>
        <linearGradient id="field" x1="0" y1="1" x2="1" y2="0">
          <stop offset="0.35" stop-color="var(--white)"/>
          <stop offset="1" stop-color="var(--tint)"/>
        </linearGradient>
        <linearGradient id="band" x1="0" y1="0" x2="1" y2="0">
          <stop offset="0" stop-color="var(--pale)"/>
          <stop offset="1" stop-color="var(--neon)"/>
        </linearGradient>
      </defs>
      <rect width="1109" height="556" fill="url(#field)"/>
      <polygon points="507,514 1109,459 1109,556 515,556" fill="url(#band)"/>
      <polygon points="55,556 507,514 515,556" fill="var(--lime)"/>
      <polygon points="0,278 55,556 37,556 0,374" fill="var(--lime)"/>
      <polygon points="0,374 37,556 31,556 0,390" fill="#9a9a9a"/>
      <polygon points="0,0 406,0 507,514 55,556 0,278" fill="var(--ink)"/>
    </svg>
  </div>

  <div class="brand-mark"></div>
  <p class="text brand-name brand-name--main">THORNWELL</p>
  <p class="text brand-name brand-name--sub">BUILDING COMPANY</p>

  <p class="text phone">472-318-6095</p>
  <p class="text licence">Lic# 5386204</p>

  <h1 class="text headline headline--top">BUILD WITH THE</h1>
  <p class="text headline headline--main">T-CREW!</p>

  <p class="text contact contact-label contact-label--email">email us:</p>
  <p class="text contact contact-value--email">thornwellbuildingcompany@mailvistra.net</p>
  <div class="contact-rule"></div>
  <p class="text contact contact-label contact-label--web">our website:</p>
  <p class="text contact contact-value--web">thornwellbuildingcompany.com</p>
</body>
</html>
```